IT Company based on Biology Business Needs a PowerPoint Design

We need a powerpoint design for a new company called 'Vast KELP'. We develop the machine learning solutions especially focused on deep learning algorithms for biology industry. Our initial product is a vision detection on biological images to help doctors diagnose the symptoms. We would like to see designs that use the color green.

Industry/Entity Type

Biotechnology

Requirements
Nice to have
• Lots of slide templates with company logo's look and feel

```html
<!DOCTYPE html>
<html lang="en">
<head>
<meta charset="utf-8">
<title>Vast KELP – Slide Templates</title>
<link rel="stylesheet" href="https://fonts.googleapis.com/css2?family=Carlito:wght@400;700&display=swap">
<style>
  :root {
    --bg: #e9ecef;
    --slide: #ffffff;
    --green-dark: #037a35;
    --green-light: #5bb534;
    --text-green: #1f8a3a;
    --text-grey: #555a5e;
  }
  * { margin: 0; padding: 0; box-sizing: border-box; }
  html, body { width: 1200px; height: 816px; overflow: hidden; background: var(--bg); }
  body { position: relative; font-family: "Carlito", "Calibri", sans-serif; }

  .slide {
    position: absolute;
    width: 346px;
    height: 270px;
    background: var(--slide);
    box-shadow: 0 2px 6px rgba(0,0,0,0.25);
    overflow: hidden;
  }
  .slide--title { left: 111px; top: 102px; }
  .slide--body { left: 724px; top: 102px; }
  .slide--closing { left: 418px; top: 533px; }

  .slide__art { position: absolute; left: 0; top: 0; width: 346px; height: 270px; }

  .brand {
    position: absolute;
    display: flex;
    align-items: center;
    gap: 4px;
    color: var(--green-light);
    font-size: 16px;
    font-weight: 400;
    white-space: nowrap;
  }
  .brand__dot { width: 9px; height: 9px; border-radius: 50%; background: var(--green-light); }
  .slide--title .brand { left: 240px; top: 44px; }
  .slide--body .brand { left: 240px; top: 44px; }
  .slide--closing .brand { left: 130px; top: 88px; }

  .slide__heading { position: absolute; color: var(--text-green); font-weight: 400; }
  .slide--title .slide__heading { left: 32px; top: 30px; font-size: 14px; }
  .slide--body .slide__heading { left: 28px; top: 50px; font-size: 14px; }

  .bullets { position: absolute; left: 53px; top: 88px; list-style: none; color: var(--text-grey); font-size: 10px; line-height: 11px; }
  .bullets li::before { content: "»"; margin-right: 6px; }

  .contact {
    position: absolute;
    left: 0; top: 138px; width: 346px;
    text-align: center;
    color: var(--text-green);
    font-size: 6.5px;
    line-height: 1;
  }
  .contact p { margin-bottom: 6px; display: flex; justify-content: center; align-items: center; gap: 3px; }
  .contact svg { width: 6px; height: 6px; fill: var(--text-green); }
</style>
</head>
<body>

<section class="slide slide--title">
  <svg class="slide__art" viewBox="0 0 346 270" aria-hidden="true">
    <path d="M0 188 Q120 232 232 256 L0 256 Z" fill="var(--green-light)"/>
    <path d="M0 220 Q170 252 346 270 L0 270 Z" fill="var(--green-dark)"/>
  </svg>
  <h1 class="slide__heading">Welcome</h1>
  <div class="brand"><span class="brand__dot"></span>Vast KELP</div>
</section>

<section class="slide slide--body">
  <svg class="slide__art" viewBox="0 0 346 270" aria-hidden="true">
    <rect x="0" y="251" width="346" height="19" fill="var(--green-dark)"/>
  </svg>
  <h2 class="slide__heading">Body Text</h2>
  <div class="brand"><span class="brand__dot"></span>Vast KELP</div>
  <ul class="bullets">
    <li>point no. 1</li>
    <li>point no. 1</li>
    <li>point no. 1</li>
    <li>point no. 1</li>
    <li>point no. 1</li>
  </ul>
</section>

<section class="slide slide--closing">
  <svg class="slide__art" viewBox="0 0 346 270" aria-hidden="true">
    <path d="M0 187 Q120 232 228 256 L0 256 Z" fill="var(--green-light)"/>
    <path d="M0 219 Q170 252 346 270 L0 270 Z" fill="var(--green-dark)"/>
  </svg>
  <div class="brand"><span class="brand__dot"></span>Vast KELP</div>
  <div class="contact">
    <p>Your Long Commercial or business address in 2 line</p>
    <p><svg viewBox="0 0 10 10"><path d="M2 1 L4 1 L5 3 L4 4 Q5 6 6 6 L7 5 L9 6 L9 8 Q8 9 7 9 Q1 8 1 2 Q1 1 2 1Z"/></svg>+00 111 222 3333</p>
    <p><svg viewBox="0 0 10 10"><path d="M0 2 H10 V8 H0 Z M0 2 L5 6 L10 2" stroke="#fff" stroke-width="0.8"/></svg>yourname@yourwebsite.com
       <svg viewBox="0 0 10 10"><circle cx="5" cy="5" r="5"/></svg>www.yourwebsite.com</p>
  </div>
</section>

</body>
</html>
```